Cedarfield Supply METAL business card

A metal business card design. Attached are older designs for a reference, but we want a NEW design, not the same as in the past. See the 2 examples just posted. We would like some cut out in the design. Possibly the pine cone or the pine tree branch (see image IMG_0).

Target Market(s)

Home and Gardern

Industry/Entity Type

Landscape

Contact Information for Business Card

Logo, website, address, name, phone numbers

```html
<!DOCTYPE html>
<html lang="en">
<head>
<meta charset="utf-8">
<title>Cedarfield Supply – Business Card</title>
<link href="https://fonts.googleapis.com/css2?family=Poppins:wght@300;400;600&family=Lobster&display=swap" rel="stylesheet">
<style>
  :root {
    --backdrop: #1e1e1e;
    --card: #0d0d0d;
    --needle-dark: #161616;
    --needle-mid: #262626;
    --orange: #f7931e;
    --grey-text: #8e8e8e;
    --light: #e6e6e6;
  }
  * { box-sizing: border-box; margin: 0; padding: 0; }
  html, body {
    width: 1200px; height: 1015px; overflow: hidden;
    background: var(--backdrop);
    font-family: "Poppins", sans-serif;
  }
  .canvas { position: relative; width: 1200px; height: 1015px; }
  .card {
    position: absolute;
    width: 600px; height: 343px;
    background: var(--card);
    overflow: hidden;
    border-radius: 4px;
  }
  .card--front { left: 90px; top: 90px; }
  .card--back  { left: 510px; top: 580px; }
  .needle-decor { position: absolute; top: 0; right: 0; width: 360px; height: 200px; }

  .brand-mark {
    position: absolute;
    display: flex; align-items: center; gap: 14px;
    color: var(--orange);
    font-family: "Poppins", sans-serif;
    font-weight: 600;
    line-height: 1.05;
  }
  .card--front .brand-mark { left: 150px; top: 130px; font-size: 40px; }
  .card--back .brand-mark { right: 40px; top: 150px; font-size: 42px; flex-direction: row-reverse; text-align: left; }
  .brand-dot { width: 18px; height: 18px; border-radius: 50%; background: var(--orange); flex: none; }

  .contact { position: absolute; left: 44px; top: 60px; }
  .contact__name {
    font-family: "Lobster", cursive;
    color: var(--orange);
    font-size: 30px;
    margin-bottom: 10px;
  }
  .rule { width: 46px; height: 2px; background: var(--orange); margin: 10px 0 12px; }
  .contact__lines { color: var(--grey-text); font-size: 15px; font-weight: 300; line-height: 1.35; }
  .social { display: flex; gap: 10px; }
  .social__item { width: 16px; height: 16px; border-radius: 50%; border: 2px solid var(--orange); }
</style>
</head>
<body>
<main class="canvas">

  <section class="card card--front" aria-label="Card front">
    <svg class="needle-decor" viewBox="0 0 360 200" role="img" aria-label="Dark tonal illustration of scattered pine needles">
      <defs>
        <linearGradient id="needleFront" x1="0" y1="0" x2="1" y2="1">
          <stop offset="0" stop-color="#1b1b1b"/>
          <stop offset="1" stop-color="#111111"/>
        </linearGradient>
      </defs>
      <polygon points="60,0 360,0 360,200 200,130 40,120" fill="url(#needleFront)"/>
    </svg>
    <div class="brand-mark">
      <span class="brand-dot"></span>
      <span>Cedarfield<br>Supply</span>
    </div>
  </section>

  <section class="card card--back" aria-label="Card back">
    <svg class="needle-decor" viewBox="0 0 360 200" role="img" aria-label="Dark tonal illustration of scattered pine needles">
      <defs>
        <linearGradient id="needleBack" x1="0" y1="0" x2="1" y2="1">
          <stop offset="0" stop-color="#1b1b1b"/>
          <stop offset="1" stop-color="#111111"/>
        </linearGradient>
      </defs>
      <polygon points="60,0 360,0 360,200 200,130 40,120" fill="url(#needleBack)"/>
    </svg>

    <div class="contact">
      <p class="contact__name">Dale Merritt</p>
      <div class="rule"></div>
      <p class="contact__lines">888.555.0142<br>601.555.0178<br>cedarfieldsupply.com</p>
      <div class="rule"></div>
      <p class="contact__lines">24 Hollow Birch Lane<br>Brookhaven, MS 39601</p>
      <div class="rule"></div>
      <div class="social" aria-label="Social media">
        <span class="social__item"></span>
        <span class="social__item"></span>
      </div>
    </div>

    <div class="brand-mark">
      <span class="brand-dot"></span>
      <span>Cedarfield<br>Supply</span>
    </div>
  </section>

</main>
</body>
</html>
```